Thornwell Building Company - advertisement poster

I am looking to print some canvas signs to advertise my general contracting company, Thornwell Building Company. The sign will measure 6' long x 3' high so the size should match that ratio. I already have a logo icon, which is the Letter 'A' and some trees that I would like to incorporate, see attached. I would also like the to have the following information listed:
1) phone number: 472-318-6095
2) email: thornwellbuildingcompany@mailvistra.net
3) website: thornwellbuildingcompany.com
4) Lic#5386204
5) I want to use this text: "BUILD WITH THE T-CREW!"

The ad should be relatively simple and clean. Black and Green are my company colors. I am open to creative ideas!

Target Market(s)

People looking to renovate their homes

Industry/Entity Type

Construction

Colors
59FF00
82FF00
B8FF75
E3FFCB
F4FFEA

Requirements
Must have
• Must have my company logo
Should not have
• No photos or complex graphics

```html
<!DOCTYPE html>
<html lang="en">
<head>
<meta charset="utf-8">
<title>Thornwell Building Company – Sign</title>
<link rel="stylesheet" href="https://fonts.googleapis.com/css2?family=Montserrat:wght@500;700;800&display=swap">
<style>
  :root {
    --backdrop: #828282;
    --brand-black: #000000;
    --brand-green: #6db345;
    --paper: #ffffff;
    --ink-light: #ffffff;
    --rule-grey: #9a9a9a;
  }
  html, body {
    margin: 0;
    padding: 0;
    width: 1200px;
    height: 1000px;
    overflow: hidden;
    background: var(--backdrop);
    font-family: "Montserrat", Arial, sans-serif;
  }
  .sign {
    position: absolute;
    left: 59px;
    top: 230px;
    width: 1082px;
    height: 540px;
    background: var(--paper);
    overflow: hidden;
  }
  .header-band {
    position: absolute;
    left: 0;
    top: 0;
    width: 1082px;
    height: 218px;
    background: var(--brand-black);
    border-radius: 0 0 235px 235px / 0 0 218px 218px;
  }
  .brand-mark {
    position: absolute;
    left: 496px;
    top: 22px;
    width: 90px;
    height: 90px;
    background: var(--brand-green);
  }
  .est-tag {
    position: absolute;
    top: 80px;
    width: 60px;
    padding: 4px 0;
    border-top: 1px solid var(--rule-grey);
    border-bottom: 1px solid var(--rule-grey);
    color: var(--ink-light);
    font-weight: 500;
    font-size: 11px;
    letter-spacing: 3px;
    text-align: center;
    line-height: 1;
  }
  .est-tag.left { left: 368px; }
  .est-tag.right { left: 648px; }
  .brand-name {
    position: absolute;
    left: 0;
    right: 0;
    top: 132px;
    margin: 0;
    text-align: center;
    color: var(--ink-light);
    font-weight: 800;
    line-height: 1;
  }
  .brand-name .primary {
    display: block;
    font-size: 48px;
    letter-spacing: 1px;
  }
  .brand-name .secondary {
    display: block;
    margin-top: 6px;
    font-size: 19px;
    letter-spacing: 7px;
  }
  .info-band {
    position: absolute;
    left: 0;
    top: 218px;
    width: 1082px;
    height: 322px;
    background: var(--brand-green);
  }
  .contact-list {
    position: absolute;
    left: 218px;
    top: 39px;
    margin: 0;
    padding: 0;
    list-style: none;
  }
  .contact-list li {
    display: flex;
    align-items: center;
    height: 43px;
    color: var(--ink-light);
    font-weight: 800;
    font-size: 25px;
    letter-spacing: 0.8px;
  }
  .contact-icon {
    width: 28px;
    height: 28px;
    margin-right: 11px;
    flex: none;
  }
  .license {
    position: absolute;
    left: 0;
    right: 0;
    top: 165px;
    margin: 0;
    text-align: center;
    color: var(--ink-light);
    font-weight: 800;
    font-size: 38px;
    letter-spacing: 2px;
  }
  .tagline {
    position: absolute;
    left: 0;
    right: 0;
    top: 240px;
    margin: 0;
    text-align: center;
    color: var(--ink-light);
    font-weight: 800;
    font-size: 56px;
    letter-spacing: 6px;
    line-height: 1.1;
  }
</style>
</head>
<body>
  <main class="sign">
    <header class="header-band">
      <div class="brand-mark" role="img" aria-label="Company logo mark"></div>
      <span class="est-tag left">ESTD</span>
      <span class="est-tag right">2020</span>
      <h1 class="brand-name">
        <span class="primary">THORNWELL</span>
        <span class="secondary">BUILDING COMPANY</span>
      </h1>
    </header>

    <section class="info-band">
      <ul class="contact-list">
        <li>
          <svg class="contact-icon" viewBox="0 0 28 28" aria-hidden="true">
            <rect width="28" height="28" rx="4" fill="#000"/>
            <rect x="9" y="5" width="10" height="18" rx="2" fill="none" stroke="#6db345" stroke-width="1.8"/>
            <circle cx="14" cy="20" r="1" fill="#6db345"/>
          </svg>
          472-318-6095
        </li>
        <li>
          <svg class="contact-icon" viewBox="0 0 28 28" aria-hidden="true">
            <rect width="28" height="28" rx="4" fill="#000"/>
            <rect x="5" y="8" width="18" height="12" fill="#6db345"/>
            <path d="M5 8 L14 15 L23 8 M5 20 L11.5 13.5 M23 20 L16.5 13.5" fill="none" stroke="#000" stroke-width="1.4"/>
          </svg>
          thornwellbuildingcompany@mailvistra.net
        </li>
        <li>
          <svg class="contact-icon" viewBox="0 0 28 28" aria-hidden="true">
            <rect width="28" height="28" rx="4" fill="#000"/>
            <g fill="none" stroke="#6db345" stroke-width="1.4">
              <circle cx="14" cy="14" r="9"/>
              <ellipse cx="14" cy="14" rx="4" ry="9"/>
              <path d="M5 14 H23 M7 9.5 H21 M7 18.5 H21"/>
            </g>
          </svg>
          www.thornwellbuildingcompany.com
        </li>
      </ul>
      <p class="license">Lic#5386204</p>
      <p class="tagline">BUILD WITH THE T-CREW!</p>
    </section>
  </main>
</body>
</html>
```